WINE LABEL for Oak-Q Vale.

We require a wine bottle label for our Oak-Q Vale brand new to the market.
A sample "mock-up" layout of the front and back label is attached. The Oak-Q writing can be a logo type design with any font the designer chooses keeping in mind this will be used on Stationary, business cards and vehicles as well so could included some creative design as long as its clear to read the "Oak-Q" We require a pair of "crusty cowboy boots" as the main theme of the label but the designer could use flair here and design inside a circle or leave as set out.The main thing is they are rugged looking. The label can be framed if appropriate and the use of a parchment look or old western looking idea could be used. We would limit colors to 3 for printing purposes so the combination of colors is up to the designer as long as it stands out on the label visually. The rear label components is attached but can be set-out in any form the designer chooses. The use of the mountain outline at the base of the rear label may add a nice addition to this as its the view we see from our vineyard. Anything else please message me directly.

Target Market(s)

Boutique vineyard label that stands out from the normal.

Contact Information for Business Card

Set out using the designs from the label.

Font styles to use
Other font styles liked:
• Designer to use their selection

Requirements
Must have
• as set out on attached label Mock-up.
• A western theme for the label is preferred.
Should not have
• photos or more than 3 colours

```html
<!DOCTYPE html>
<html lang="en">
<head>
<meta charset="utf-8">
<title>Oak-Q Vale – Pinot Noir Label</title>
<link href="https://fonts.googleapis.com/css2?family=Germania+One&display=swap" rel="stylesheet">
<style>
  :root {
    --ink: #111111;
    --red: #c8372d;
    --paper: #ffffff;
    --leather-dark: #5a4630;
    --leather-light: #a88a63;
    --ornament: #d9d9d9;
  }
  html, body {
    margin: 0;
    padding: 0;
    overflow: hidden;
    background: var(--paper);
  }
  .label {
    position: relative;
    width: 838px;
    height: 1200px;
    background: var(--paper);
    font-family: "Germania One", "Impact", sans-serif;
    color: var(--ink);
    overflow: hidden;
  }
  .frame-outer {
    position: absolute;
    left: 22px; top: 22px;
    width: 784px; height: 1146px;
    border: 5px solid var(--ink);
  }
  .frame-inner {
    position: absolute;
    left: 34px; top: 34px;
    width: 766px; height: 1128px;
    border: 2px solid var(--ink);
  }
  .corner-ornament {
    position: absolute;
    width: 44px;
    height: 84px;
    background: var(--ornament);
  }
  .corner-ornament.tl { left: 48px; top: 48px; }
  .corner-ornament.tr { right: 48px; top: 48px; }
  .corner-ornament.bl { left: 48px; bottom: 48px; }
  .corner-ornament.br { right: 48px; bottom: 48px; }

  .brand-name {
    position: absolute;
    left: 0; right: 0;
    top: 150px;
    text-align: center;
    color: var(--red);
    font-weight: 400;
    line-height: 0.95;
    letter-spacing: 4px;
    text-transform: uppercase;
  }
  .brand-name .line-main { display: block; font-size: 190px; }
  .brand-name .line-sub { display: block; font-size: 110px; }

  .boots-illustration {
    position: absolute;
    left: 276px; top: 512px;
    width: 308px; height: 224px;
    border-radius: 6px;
    background: linear-gradient(160deg, var(--leather-light), var(--leather-dark));
  }

  .region {
    position: absolute;
    left: 0; right: 0;
    text-align: center;
    text-transform: uppercase;
  }
  .region-valley { top: 748px; font-size: 66px; letter-spacing: 1px; }
  .region-area { top: 862px; font-size: 44px; }
  .leaf-ornament {
    position: absolute;
    top: 828px;
    width: 82px; height: 28px;
    background: var(--ornament);
  }
  .leaf-ornament.left { left: 206px; }
  .leaf-ornament.right { right: 206px; }

  .varietal-detail { top: 936px; font-size: 30px; }
  .varietal { top: 980px; font-size: 42px; text-transform: none; }
  .vintage { top: 1030px; font-size: 46px; }
  .vintage-ornament {
    position: absolute;
    top: 1048px;
    width: 34px; height: 18px;
    background: var(--ornament);
  }
  .vintage-ornament.left { left: 322px; }
  .vintage-ornament.right { right: 322px; }

  .origin-banner {
    position: absolute;
    left: 260px; top: 1090px;
    width: 318px; height: 46px;
  }
  .origin-banner svg { position: absolute; inset: 0; }
  .origin-banner span {
    position: relative;
    display: block;
    text-align: center;
    line-height: 46px;
    font-size: 30px;
  }
</style>
</head>
<body>
<div class="label">
  <div class="frame-outer"></div>
  <div class="frame-inner"></div>

  <div class="corner-ornament tl" role="img" aria-label="Corner scroll ornament"></div>
  <div class="corner-ornament tr" role="img" aria-label="Corner scroll ornament"></div>
  <div class="corner-ornament bl" role="img" aria-label="Corner scroll ornament"></div>
  <div class="corner-ornament br" role="img" aria-label="Corner scroll ornament"></div>

  <h1 class="brand-name">
    <span class="line-main">Oak-Q</span>
    <span class="line-sub">Vale</span>
  </h1>

  <div class="boots-illustration" role="img" aria-label="Illustration of a pair of worn, rugged leather cowboy work boots with loose laces"></div>

  <div class="region region-valley">Waitaki Valley</div>
  <div class="leaf-ornament left" role="img" aria-label="Oak leaf and acorn ornament"></div>
  <div class="leaf-ornament right" role="img" aria-label="Oak leaf and acorn ornament"></div>
  <div class="region region-area">North Otago</div>

  <div class="region varietal-detail">Single Vinyard</div>
  <div class="region varietal">Pinot Noir</div>
  <div class="vintage-ornament left" role="img" aria-label="Small flourish ornament"></div>
  <div class="vintage-ornament right" role="img" aria-label="Small flourish ornament"></div>
  <div class="region vintage">2016</div>

  <div class="origin-banner">
    <svg width="318" height="46" viewBox="0 0 318 46" aria-hidden="true">
      <polygon points="2,2 316,2 306,23 316,44 2,44 12,23" fill="var(--paper)" stroke="var(--ink)" stroke-width="3"/>
    </svg>
    <span>New Zealand Wine</span>
  </div>
</div>
</body>
</html>
```